We are looking to create a graphic that will be used in Facebook posts each week to show the daily Porchlight Report. Attached is an example of what we are looking for. We need to be able to update the forecast. So we will need hi-res vector files. The graphics need to represent the level of mosquito activity: SLIGHT, AVERAGE, INTENSE, EXTREME

```html
<!DOCTYPE html>
<html lang="en">
<head>
<meta charset="utf-8">
<title>Porchlight Report – Weekly Forecast Graphic</title>
<link rel="stylesheet" href="https://fonts.googleapis.com/css2?family=Open+Sans:wght@700&family=Montserrat:wght@600;800&family=Arvo:wght@400;700&family=Roboto+Condensed:wght@400;500&display=swap">
<style>
  :root{
    --board-top:#d3d4d6;
    --board-bottom:#c5c6c8;
    --band:#dcdddf;
    --title-ink:#1f2a10;
    --revision-ink:#1d4a2a;
    --panel:#ffffff;
    --rule:#c7c9cc;
    --ink:#1b1b1b;
    --muted:#555;
    --slight:#1e9a4a;
    --slight-light:#2fbf61;
    --average:#f6b400;
    --average-light:#ffd21f;
    --intense:#e4672a;
    --intense-light:#f5893f;
    --extreme:#d41f2a;
    --extreme-light:#ee3a3f;
    --idle:#c9ccd1;
    --gauge-line:#2b2b2b;
  }
  *{box-sizing:border-box;margin:0;padding:0}
  html,body{width:1200px;height:781px;overflow:hidden}
  body{
    position:relative;
    background:linear-gradient(180deg,var(--board-top),var(--board-bottom));
    font-family:"Roboto Condensed",sans-serif;
  }
  .board-title{
    position:absolute;top:48px;left:0;width:1200px;text-align:center;
    font-family:"Open Sans",sans-serif;font-weight:700;font-size:56px;
    color:var(--title-ink);letter-spacing:-.5px;line-height:1;
  }
  .revision-band{
    position:absolute;top:134px;left:40px;width:1160px;height:58px;
    background:var(--band);display:flex;align-items:center;justify-content:center;
  }
  .revision-band p{
    font-family:"Montserrat",sans-serif;font-weight:600;font-size:27px;
    color:var(--revision-ink);letter-spacing:.5px;margin-left:-40px;
  }

  .forecast-graphic{
    position:absolute;left:118px;top:254px;width:964px;height:504px;overflow:hidden;
  }
  .backdrop{
    position:absolute;inset:0;
    background:
      radial-gradient(ellipse 40% 30% at 50% 30%,rgba(80,88,86,.9),rgba(80,88,86,0) 70%),
      linear-gradient(180deg,#8d9a9b 0%,#5d6661 30%,#3f4a3c 52%,#2f4a26 72%,#3d7a24 88%,#4f8f2c 100%);
  }
  .headline{
    position:absolute;top:70px;left:0;width:100%;text-align:center;
    font-family:"Montserrat",sans-serif;font-weight:800;font-size:76px;line-height:1;
    color:#fff;letter-spacing:-3px;text-shadow:2px 3px 4px rgba(0,0,0,.45);
  }
  .region{
    position:absolute;top:148px;left:0;width:100%;text-align:center;
    font-family:"Arvo",serif;font-size:36px;color:#fff;letter-spacing:.5px;
    text-shadow:1px 2px 3px rgba(0,0,0,.4);
  }
  .forecast-panel{
    position:absolute;left:19px;top:211px;width:925px;height:260px;background:var(--panel);
  }
  .week{
    position:absolute;left:13px;top:0;width:902px;height:218px;
    display:grid;grid-template-columns:repeat(7,1fr);
    border-bottom:1px solid var(--rule);
  }
  .day{position:relative;text-align:center}
  .day + .day::before{
    content:"";position:absolute;left:0;top:50px;bottom:0;border-left:1px solid var(--rule);
  }
  .day-name{
    margin-top:33px;font-family:"Arvo",serif;font-size:13px;color:var(--ink);line-height:1;
  }
  .day-date{margin-top:6px;font-size:9.5px;color:var(--muted);line-height:1}
  .gauge{display:block;width:104px;height:104px;margin:15px auto 0}
  .level{
    display:block;width:90px;height:20px;margin:1px auto 0;border-radius:10px;
    font-size:8.5px;font-weight:500;letter-spacing:.6px;line-height:20px;color:#fff;
  }
  .level--slight{background:linear-gradient(180deg,var(--slight-light),var(--slight))}
  .level--average{background:linear-gradient(180deg,var(--average-light),var(--average))}
  .level--intense{background:linear-gradient(180deg,var(--intense-light),var(--intense))}
  .level--extreme{background:linear-gradient(180deg,var(--extreme-light),var(--extreme))}

  .legend{
    position:absolute;top:229px;left:278px;display:flex;align-items:center;gap:8px;
    font-size:10.5px;color:var(--ink);letter-spacing:.3px;
  }
  .legend-item{display:flex;align-items:center;gap:13px;margin-right:0}
  .legend-item + .legend-item{margin-left:0}
  .swatch{width:40px;height:12px}
  .swatch--slight{background:linear-gradient(180deg,var(--slight-light),var(--slight))}
  .swatch--average{background:linear-gradient(180deg,var(--average-light),var(--average))}
  .swatch--intense{background:linear-gradient(180deg,var(--intense-light),var(--intense))}
  .swatch--extreme{background:linear-gradient(180deg,var(--extreme-light),var(--extreme))}
  .sprite{position:absolute;width:0;height:0;overflow:hidden}
</style>
</head>
<body>
  <h1 class="board-title">Porchlight Report</h1>
  <div class="revision-band"><p>Revision 1- Mockup 3a</p></div>

  <svg class="sprite" aria-hidden="true">
    <defs>
      <radialGradient id="core-slight" cx="45%" cy="40%" r="65%"><stop offset="0" stop-color="#3ccf6e"/><stop offset="1" stop-color="#137a38"/></radialGradient>
      <radialGradient id="core-average" cx="45%" cy="40%" r="65%"><stop offset="0" stop-color="#ffe04a"/><stop offset="1" stop-color="#f2a100"/></radialGradient>
      <radialGradient id="core-intense" cx="45%" cy="40%" r="65%"><stop offset="0" stop-color="#f89a4c"/><stop offset="1" stop-color="#d9551f"/></radialGradient>
      <radialGradient id="core-extreme" cx="45%" cy="40%" r="65%"><stop offset="0" stop-color="#f2494c"/><stop offset="1" stop-color="#c0141f"/></radialGradient>

      <g id="dial-frame">
        <circle r="50" fill="none" stroke="var(--gauge-line)" stroke-width="1.6" stroke-dasharray="235.6 400" transform="rotate(135)"/>
        <circle r="36" fill="none" stroke="var(--gauge-line)" stroke-width="1.2" stroke-dasharray="169.6 400" transform="rotate(135)"/>
      </g>

      <symbol id="gauge-slight" viewBox="-55 -55 110 110">
        <use href="#dial-frame"/>
        <g fill="none" stroke-width="10" stroke-dasharray="31.5 300">
          <circle r="43" stroke="var(--slight)" transform="rotate(136)"/>
          <circle r="43" stroke="var(--idle)" transform="rotate(181)"/>
          <circle r="43" stroke="var(--idle)" transform="rotate(226)"/>
          <circle r="43" stroke="var(--idle)" transform="rotate(271)"/>
          <circle r="43" stroke="var(--idle)" transform="rotate(316)"/>
          <circle r="43" stroke="var(--idle)" transform="rotate(361)"/>
        </g>
        <circle r="32" fill="#fff" stroke="var(--gauge-line)" stroke-width="1"/>
        <circle r="28" fill="url(#core-slight)"/>
      </symbol>

      <symbol id="gauge-average" viewBox="-55 -55 110 110">
        <use href="#dial-frame"/>
        <g fill="none" stroke-width="10" stroke-dasharray="31.5 300">
          <circle r="43" stroke="var(--slight)" transform="rotate(136)"/>
          <circle r="43" stroke="var(--average)" transform="rotate(181)"/>
          <circle r="43" stroke="var(--average)" transform="rotate(226)"/>
          <circle r="43" stroke="var(--idle)" transform="rotate(271)"/>
          <circle r="43" stroke="var(--idle)" transform="rotate(316)"/>
          <circle r="43" stroke="var(--idle)" transform="rotate(361)"/>
        </g>
        <circle r="32" fill="#fff" stroke="var(--gauge-line)" stroke-width="1"/>
        <circle r="28" fill="url(#core-average)"/>
      </symbol>

      <symbol id="gauge-intense" viewBox="-55 -55 110 110">
        <use href="#dial-frame"/>
        <g fill="none" stroke-width="10" stroke-dasharray="31.5 300">
          <circle r="43" stroke="var(--slight)" transform="rotate(136)"/>
          <circle r="43" stroke="var(--average)" transform="rotate(181)"/>
          <circle r="43" stroke="var(--average)" transform="rotate(226)"/>
          <circle r="43" stroke="var(--intense)" transform="rotate(271)"/>
          <circle r="43" stroke="var(--intense)" transform="rotate(316)"/>
          <circle r="43" stroke="var(--idle)" transform="rotate(361)"/>
        </g>
        <circle r="32" fill="#fff" stroke="var(--gauge-line)" stroke-width="1"/>
        <circle r="28" fill="url(#core-intense)"/>
      </symbol>

      <symbol id="gauge-extreme" viewBox="-55 -55 110 110">
        <use href="#dial-frame"/>
        <g fill="none" stroke-width="10" stroke-dasharray="31.5 300">
          <circle r="43" stroke="var(--slight)" transform="rotate(136)"/>
          <circle r="43" stroke="var(--average)" transform="rotate(181)"/>
          <circle r="43" stroke="var(--average)" transform="rotate(226)"/>
          <circle r="43" stroke="var(--intense)" transform="rotate(271)"/>
          <circle r="43" stroke="var(--intense)" transform="rotate(316)"/>
          <circle r="43" stroke="var(--extreme)" transform="rotate(361)"/>
        </g>
        <circle r="32" fill="#fff" stroke="var(--gauge-line)" stroke-width="1"/>
        <circle r="28" fill="url(#core-extreme)"/>
      </symbol>
    </defs>
  </svg>

  <section class="forecast-graphic">
    <div class="backdrop" role="img" aria-label="Photo of a suburban house behind tall green grass, softly blurred"></div>
    <h2 class="headline">PORCHLIGHT REPORT</h2>
    <p class="region">Greater Milwakukee</p>

    <div class="forecast-panel">
      <div class="week">
        <div class="day">
          <p class="day-name">Mon Day</p><p class="day-date">02/20</p>
          <svg class="gauge" role="img" aria-label="Slight activity gauge with mosquito illustration in the centre"><use href="#gauge-slight"/></svg>
          <span class="level level--slight">SLIGHT</span>
        </div>
        <div class="day">
          <p class="day-name">Tues Day</p><p class="day-date">02/21</p>
          <svg class="gauge" role="img" aria-label="Average activity gauge with mosquito illustration in the centre"><use href="#gauge-average"/></svg>
          <span class="level level--average">AVERAGE</span>
        </div>
        <div class="day">
          <p class="day-name">Wednes Day</p><p class="day-date">02/22</p>
          <svg class="gauge" role="img" aria-label="Intense activity gauge with mosquito illustration in the centre"><use href="#gauge-intense"/></svg>
          <span class="level level--intense">INTENSE</span>
        </div>
        <div class="day">
          <p class="day-name">Thurs Day</p><p class="day-date">02/23</p>
          <svg class="gauge" role="img" aria-label="Extreme activity gauge with mosquito illustration in the centre"><use href="#gauge-extreme"/></svg>
          <span class="level level--extreme">EXTREME</span>
        </div>
        <div class="day">
          <p class="day-name">Fri Day</p><p class="day-date">02/24</p>
          <svg class="gauge" role="img" aria-label="Average activity gauge with mosquito illustration in the centre"><use href="#gauge-average"/></svg>
          <span class="level level--average">AVERAGE</span>
        </div>
        <div class="day">
          <p class="day-name">Satur Day</p><p class="day-date">02/25</p>
          <svg class="gauge" role="img" aria-label="Intense activity gauge with mosquito illustration in the centre"><use href="#gauge-intense"/></svg>
          <span class="level level--intense">INTENSE</span>
        </div>
        <div class="day">
          <p class="day-name">Sun Day</p><p class="day-date">02/26</p>
          <svg class="gauge" role="img" aria-label="Slight activity gauge with mosquito illustration in the centre"><use href="#gauge-slight"/></svg>
          <span class="level level--slight">SLIGHT</span>
        </div>
      </div>

      <div class="legend">
        <span class="legend-item"><i class="swatch swatch--slight"></i>Slight</span>
        <span class="legend-item"><i class="swatch swatch--average"></i>Average</span>
        <span class="legend-item"><i class="swatch swatch--intense"></i>Intense</span>
        <span class="legend-item"><i class="swatch swatch--extreme"></i>Extreme</span>
      </div>
    </div>
  </section>
</body>
</html>
```